Global investment holding company - Business Card Design

Brenvik Holdings is a recently incorporated investment holding company. Based in Singapore, it has operations in global emerging markets in the transport & logistics, energy and livestock industries.

Its tagline "Partners in Shared Growth" reflects the company's philosophy of helping countries progress through partnerships which generate employment and share benefits with its society.

We are looking for a business card that reflects our global presence - incorporating the logo design into the business card design. It must have a sophisticated, modern & corporate feel.

Target Market(s)

Investors and high level governmental officials

Industry/Entity Type

Investment

Requirements
Must have
• - Use of shades of blue in logo

-Profile picture

- Name: Dennis Okoro
- Title: Chairman
- Email: dennis@brenvikholdings.example
- Mob: +65 9154 6081
- Tel: +65 6419 5820
- DID: + 65 6419 5821
- Address: 47 Marlow Road, #05-03, Singapore 048812

- website: www.brenvikholdings.example

```html
<!DOCTYPE html>
<html lang="en">
<head>
<meta charset="utf-8">
<title>Brenvik Holdings – Business Card</title>
<link href="https://fonts.googleapis.com/css2?family=Lato:wght@400;700&family=Arimo:wght@400;700&display=swap" rel="stylesheet">
<style>
  :root {
    --stage: #3b3b3d;
    --card-dark: #16181b;
    --card-light: #ffffff;
    --frame-blue: #1f4f8f;
    --brand-blue: #1d4f91;
    --band-blue: #1b4a8c;
    --circle-blue: #3d8fc9;
    --ink-blue: #1f3f8a;
    --ink-grey: #555a60;
    --tagline-grey: #7a7f85;
    --tagline-dark: #8a8f94;
    --web-dark: #6b7076;
  }
  * { box-sizing: border-box; margin: 0; padding: 0; }
  html, body { width: 1200px; height: 534px; overflow: hidden; }
  body { background: var(--stage); position: relative; font-family: "Arimo", Arial, sans-serif; }

  .card {
    position: absolute;
    top: 121px;
    width: 514px;
    height: 291px;
    border: 5px solid var(--frame-blue);
    border-radius: 20px;
    overflow: hidden;
  }
  .card--front { left: 64px; background: var(--card-dark); }
  .card--back { left: 621px; background: var(--card-light); }

  /* brand lockup */
  .brand { position: absolute; display: flex; align-items: center; }
  .brand__mark { border-radius: 50%; background: var(--circle-blue); flex: none; }
  .brand__name {
    font-family: "Lato", sans-serif;
    font-weight: 700;
    color: var(--brand-blue);
    text-transform: uppercase;
    line-height: 1;
  }
  .tagline {
    position: absolute;
    font-family: "Lato", sans-serif;
    text-transform: uppercase;
    letter-spacing: 1px;
    white-space: nowrap;
  }

  /* front */
  .card--front .brand { left: 118px; top: 78px; gap: 20px; }
  .card--front .brand__mark { width: 92px; height: 92px; }
  .card--front .brand__name { font-size: 34px; }
  .card--front .tagline {
    left: 0; right: 0; top: 187px; text-align: center;
    font-size: 17px; color: var(--tagline-dark);
  }
  .card--front .website {
    position: absolute; left: 0; right: 0; top: 224px; text-align: center;
    font-family: "Lato", sans-serif; font-size: 11px; letter-spacing: 3px;
    color: var(--web-dark);
  }

  /* back */
  .band {
    position: absolute; left: 0; right: 0; top: 166px; height: 40px;
    background: var(--band-blue);
  }
  .portrait {
    position: absolute; left: 40px; top: 45px; width: 118px; height: 140px;
    border: 4px solid #ffffff;
    box-shadow: 0 2px 6px rgba(0,0,0,0.35);
    background: linear-gradient(160deg, #8a8d8e 0%, #c7a98e 45%, #2c3340 100%);
  }
  .card--back .brand { left: 180px; top: 56px; gap: 16px; }
  .card--back .brand__mark { width: 70px; height: 70px; }
  .card--back .brand__name { font-size: 27px; }
  .card--back .tagline {
    left: 185px; top: 142px; font-size: 13px; color: var(--tagline-grey);
  }
  .person {
    position: absolute; left: 190px; top: 166px; height: 40px;
    display: flex; align-items: center; color: #ffffff;
  }
  .person__name { font-size: 19px; font-weight: 700; text-transform: uppercase; letter-spacing: 0.5px; }
  .person__title {
    font-size: 12px; text-transform: uppercase; margin-left: 8px; padding-left: 8px;
    border-left: 1px solid rgba(255,255,255,0.7); line-height: 14px;
  }
  .contact {
    position: absolute; left: 0; right: 0; top: 222px; text-align: center;
    color: var(--ink-blue);
  }
  .contact__address { font-size: 14px; margin-bottom: 4px; }
  .contact__line { font-size: 12.5px; margin-bottom: 3px; white-space: nowrap; }
  .contact__label { color: var(--ink-grey); }
  .contact__sep { color: #9aa0a6; margin: 0 5px; }
</style>
</head>
<body>

  <section class="card card--front">
    <div class="brand">
      <span class="brand__mark"></span>
      <span class="brand__name">Brenvik<br>Holdings</span>
    </div>
    <p class="tagline">Partners in Shared Growth</p>
    <p class="website">www.brenvikholdings.example</p>
  </section>

  <section class="card card--back">
    <div class="band"></div>
    <div class="portrait" role="img" aria-label="Profile photo of Dennis Okoro, Chairman"></div>
    <div class="brand">
      <span class="brand__mark"></span>
      <span class="brand__name">Brenvik<br>Holdings</span>
    </div>
    <p class="tagline">Partners in Shared Growth</p>
    <div class="person">
      <span class="person__name">Dennis Okoro</span>
      <span class="person__title">Chairman</span>
    </div>
    <div class="contact">
      <p class="contact__address">47 Marlow Road, #05-03, Singapore 048812</p>
      <p class="contact__line">
        <span class="contact__label">mobile:</span> +65 9154 6081<span class="contact__sep">|</span>
        <span class="contact__label">tel:</span> +65 6419 5820<span class="contact__sep">|</span>
        <span class="contact__label">did:</span> + 65 6419 5821
      </p>
      <p class="contact__line">
        <span class="contact__label">email:</span> dennis@brenvikholdings.example<span class="contact__sep">|</span>
        <span class="contact__label">web:</span> www.brenvikholdings.example
      </p>
    </div>
  </section>

</body>
</html>
```